Business card - Brio Margin - size 85 mm * 55 mm

We need new business cards. Design must fit with our vision of the firm. You find in the attached file our logo and a short description of our firm (mission, vision, value, business and so on).

Target Market(s)

Consulting firm in performance improvement

Industry/Entity Type

Management Consulting

Contact Information for Business Card

SIZE
85 mm * 55 mm
INFORMATIONS
name surname
role position
telephone number
email address

Requirements
Must have
• the brand must APPEAR for the rest Would we like to have something sleek, inspired to a "just right" approach
Should not have
• Please avoid the black color as background

```html
<!DOCTYPE html>
<html lang="en">
<head>
<meta charset="utf-8">
<title>Brio Margin – Business Card</title>
<link href="https://fonts.googleapis.com/css2?family=Exo+2:wght@600&family=Roboto:wght@300;400&display=swap" rel="stylesheet">
<style>
  :root {
    --page-bg: #e4e4e4;
    --green-light: #9fd33f;
    --green-mid: #7cc12b;
    --green-dark: #4e9c14;
    --accent-orange: #e8641b;
    --paper: #ffffff;
    --ink-dark: #4a4a4a;
    --ink-body: #333333;
    --ink-muted: #777777;
  }
  * { box-sizing: border-box; margin: 0; padding: 0; }
  html, body { width: 1200px; height: 852px; overflow: hidden; }
  body {
    background: var(--page-bg);
    font-family: "Roboto", Arial, sans-serif;
    position: relative;
  }
  .card {
    position: absolute;
    top: 264px;
    width: 500px;
    height: 324px;
    border-radius: 16px;
    overflow: hidden;
    box-shadow: 0 4px 14px rgba(0,0,0,.18);
  }
  /* Front */
  .card-front {
    left: 60px;
    background: linear-gradient(160deg, var(--green-light) 0%, var(--green-mid) 55%, var(--green-dark) 100%);
    border-bottom: 7px solid var(--accent-orange);
  }
  .front-brand {
    position: absolute;
    inset: 0;
    display: flex;
    flex-direction: column;
    align-items: center;
    justify-content: center;
    gap: 22px;
    color: var(--paper);
  }
  .brand-circle {
    width: 96px; height: 96px;
    border: 4px solid var(--paper);
    border-radius: 50%;
  }
  .brand-name {
    font-weight: 300;
    font-size: 20px;
    letter-spacing: 10px;
    text-transform: uppercase;
    padding-left: 10px;
  }
  /* Back */
  .card-back { left: 640px; background: var(--paper); }
  .card-back svg.back-shape { position: absolute; inset: 0; }
  .back-brand {
    position: absolute;
    left: 34px; top: 118px;
    display: flex; align-items: center; gap: 10px;
    color: var(--paper);
    font-weight: 400;
    font-size: 17px;
    letter-spacing: 2px;
    text-transform: uppercase;
  }
  .back-brand .brand-circle { width: 40px; height: 40px; border-width: 3px; }
  .person {
    position: absolute;
    right: 28px; top: 30px;
    text-align: right;
  }
  .person-name {
    font-family: "Exo 2", Arial, sans-serif;
    font-weight: 600;
    font-size: 22px;
    color: var(--ink-dark);
  }
  .person-role { font-size: 12px; color: var(--ink-muted); margin-top: 1px; }
  .contact {
    position: absolute;
    right: 26px; bottom: 36px;
    list-style: none;
    text-align: right;
    font-size: 13px;
    line-height: 21px;
    color: var(--ink-body);
  }
  .contact li { display: flex; justify-content: flex-end; align-items: center; gap: 8px; }
  .contact .icon { width: 14px; height: 14px; flex: none; }
  .contact .icon-gap { width: 14px; flex: none; }
</style>
</head>
<body>

  <section class="card card-front" aria-label="Card front">
    <div class="front-brand">
      <div class="brand-circle"></div>
      <div class="brand-name">Brio Margin</div>
    </div>
  </section>

  <section class="card card-back" aria-label="Card back">
    <svg class="back-shape" viewBox="0 0 500 324" width="500" height="324" aria-hidden="true">
      <defs>
        <linearGradient id="backGreen" x1="0" y1="0" x2="0.4" y2="1">
          <stop offset="0" stop-color="#9fd33f"/>
          <stop offset="0.55" stop-color="#7cc12b"/>
          <stop offset="1" stop-color="#4e9c14"/>
        </linearGradient>
      </defs>
      <path d="M0,0 H228 C262,70 296,190 300,324 H0 Z" fill="#e8641b"/>
      <path d="M0,0 H220 C254,70 288,190 292,324 H0 Z" fill="url(#backGreen)"/>
    </svg>

    <div class="back-brand">
      <div class="brand-circle"></div>
      <span>Brio Margin</span>
    </div>

    <div class="person">
      <div class="person-name">Lena Hartwell</div>
      <div class="person-role">Managing Director</div>
    </div>

    <ul class="contact">
      <li>418 Orchard Lane No.27<span class="icon-gap"></span></li>
      <li>Fairbrook Oregon 97410
        <svg class="icon" viewBox="0 0 14 14" aria-hidden="true"><rect x="3.5" y="0.5" width="7" height="13" rx="1.5" fill="#7cc12b"/><rect x="5" y="2.5" width="4" height="7" fill="#fff"/></svg>
      </li>
      <li>+111 480 2716
        <svg class="icon" viewBox="0 0 14 14" aria-hidden="true"><path d="M3 1 L6 4 L4.5 5.5 C5.5 7.5 6.5 8.5 8.5 9.5 L10 8 L13 11 L11 13 C6 12 2 8 1 3 Z" fill="#7cc12b"/></svg>
      </li>
      <li>www.briomargin.com<span class="icon-gap"></span></li>
      <li>lena@briomargin.com
        <svg class="icon" viewBox="0 0 14 14" aria-hidden="true"><rect x="0.5" y="2.5" width="13" height="9" rx="1" fill="#7cc12b"/><path d="M1 3.5 L7 8 L13 3.5" fill="none" stroke="#fff" stroke-width="1.2"/></svg>
      </li>
    </ul>
  </section>

</body>
</html>
```